Talent Management Company Needs Business Cards

Using one of the logos provided (attached) K&R Talent Collective needs a business card designed.
Please visit our website for more information about us-

www.krtalentcollective.example

The face should feature a dramatic presentation of the logo with the back being reserved for our professional information which is:

The information should be:
Dorian T. Vickers
C.E.O
Email: dtvickers@krtalentcollective.example
Mobile: 555-804-2917
Website: www.krtalentcollective.example

Marcus L. Vickers
Director of Public Relations
Email: mlvickers@krtalentcollective.example
Mobile: 555-806-3350

Jules R. Hampton
Director of Client Development
Email: jhampton@krtalentcollective.example

Simon Hurlock
Director of Brand Development
Email: shurlock@krtalentcollective.example

Would like the logo to have color. I would like to see one side red or black and the other side white but if it looks better in either black or red that would be fine to but would like to see how it comes out.

Please feel free to message me and if you would like just the icon alone I have other image files that I can send as well.

Target Market(s)

Professional Athletes, coaches, entertainers age 18-35 but also must be accepted in the business community

Industry/Entity Type

Business

Requirements
Must have
• 1) Use the logo
2) Double sided
3) Distinctive
Nice to have
• Small simple images for telephone, e-mail, and Url.

```html
<!DOCTYPE html>
<html lang="en">
<head>
<meta charset="utf-8">
<title>K&amp;R Talent Collective — Business Card</title>
<link rel="stylesheet" href="https://fonts.googleapis.com/css2?family=Arimo:wght@400;700&display=swap">
<style>
  :root {
    --backdrop: #8e8d88;
    --paper: #f3f3f4;
    --ink-dark: #1f1f21;
    --stripe: #141414;
    --red-bright: #d51f2a;
    --red-mid: #a8101b;
    --red-deep: #5e0309;
    --name-ink: #1c0608;
    --soft-text: #f4d6d8;
    --white: #ffffff;
  }
  * { box-sizing: border-box; margin: 0; padding: 0; }
  html, body { width: 1200px; height: 792px; overflow: hidden; }
  body {
    background: var(--backdrop);
    font-family: "Arimo", Arial, sans-serif;
    display: flex;
    flex-direction: column;
    align-items: center;
    justify-content: center;
    gap: 30px;
  }
  .card {
    position: relative;
    width: 620px;
    height: 354px;
    overflow: hidden;
    box-shadow: 0 6px 18px rgba(0,0,0,0.28);
  }

  /* Information side */
  .card-info { background: var(--paper); }
  .info-header {
    position: absolute; left: 0; top: 0; width: 100%; height: 150px;
    background: linear-gradient(180deg, #ffffff 0%, var(--paper) 100%);
    display: flex; align-items: center; padding-left: 36px; gap: 16px;
  }
  .brand-square { width: 46px; height: 46px; background: var(--red-mid); flex: none; }
  .brand-name {
    font-size: 28px; font-weight: 700; color: var(--ink-dark);
    text-transform: uppercase; letter-spacing: 0.5px;
  }
  .info-stripe {
    position: absolute; left: 0; top: 150px; width: 100%; height: 7px;
    background: var(--stripe);
  }
  .info-body {
    position: absolute; left: 0; top: 157px; width: 100%; height: 197px;
    background: linear-gradient(160deg, var(--red-bright) 0%, var(--red-mid) 55%, var(--red-deep) 100%);
  }
  .edge-notch {
    position: absolute; left: 0; top: 92px;
    width: 0; height: 0;
    border-top: 9px solid transparent;
    border-bottom: 9px solid transparent;
    border-left: 10px solid var(--stripe);
  }
  .person { position: absolute; left: 36px; top: 88px; }
  .person-name { font-size: 20px; font-weight: 700; color: var(--name-ink); }
  .person-title { margin-top: 10px; font-size: 14px; color: var(--soft-text); letter-spacing: 0.5px; }
  .divider {
    position: absolute; left: 250px; top: 24px; width: 1px; height: 140px;
    background: rgba(30,5,8,0.8);
  }
  .contacts { position: absolute; left: 272px; top: 30px; list-style: none; }
  .contact {
    display: flex; align-items: center; gap: 10px;
    font-size: 14px; color: var(--white); height: 26px;
  }
  .contact svg { width: 16px; height: 16px; flex: none; }

  /* Logo side */
  .card-face {
    background: radial-gradient(ellipse at 30% 20%, var(--red-bright) 0%, var(--red-mid) 50%, var(--red-deep) 100%);
  }
  .face-name {
    position: absolute; left: 300px; top: 160px;
    font-size: 26px; font-weight: 400; color: var(--white);
    text-transform: uppercase; letter-spacing: 1px;
  }
</style>
</head>
<body>

  <section class="card card-info" aria-label="Business card, contact side">
    <header class="info-header">
      <span class="brand-square" aria-hidden="true"></span>
      <span class="brand-name">K&amp;R Talent Collective</span>
    </header>
    <div class="info-stripe"></div>
    <div class="info-body">
      <span class="edge-notch" aria-hidden="true"></span>
      <div class="person">
        <p class="person-name">Dorian T. Vickers</p>
        <p class="person-title">C.E.O</p>
      </div>
      <span class="divider" aria-hidden="true"></span>
      <ul class="contacts">
        <li class="contact">
          <svg viewBox="0 0 16 16" aria-hidden="true"><rect x="4" y="1" width="8" height="14" rx="1.5" fill="none" stroke="#fff" stroke-width="1.3"/><line x1="7" y1="12.5" x2="9" y2="12.5" stroke="#fff" stroke-width="1.3"/></svg>
          <span>555-804-2917</span>
        </li>
        <li class="contact">
          <svg viewBox="0 0 16 16" aria-hidden="true"><circle cx="8" cy="8" r="2.6" fill="none" stroke="#fff" stroke-width="1.6"/><path d="M10.6 5.5v3.6c0 1.4 2.6 1.4 2.6-1.1A5.2 5.2 0 1 0 10.8 12.4" fill="none" stroke="#fff" stroke-width="1.6"/></svg>
          <span>dtvickers@krtalentcollective.example</span>
        </li>
        <li class="contact">
          <svg viewBox="0 0 16 16" aria-hidden="true"><circle cx="8" cy="8" r="6.3" fill="none" stroke="#fff" stroke-width="1.2"/><ellipse cx="8" cy="8" rx="2.8" ry="6.3" fill="none" stroke="#fff" stroke-width="1.1"/><line x1="1.7" y1="8" x2="14.3" y2="8" stroke="#fff" stroke-width="1.1"/></svg>
          <span>www.krtalentcollective.example</span>
        </li>
      </ul>
    </div>
  </section>

  <section class="card card-face" aria-label="Business card, brand side">
    <p class="face-name">K&amp;R Talent Collective</p>
  </section>

</body>
</html>
```